Online Marketing Agency Website

We are an online marketing agency that specializes in search marketing (SEM) for businesses of all sizes. Our core services include local search marketing, seo, paid search, paid social, graphic design, video production/editing and website design. We have an existing website that we launched a number of years ago but it's very outdated and we're currently too busy to design a new version.

Target Market(s)

Any business that needs online marketing services with an emphasis on search marketing.

Industry/Entity Type

Ad Agency

Number of Pages Required

4 page

Font styles to use
Sans Serif

Requirements
Must have
• Home page, interior page, blog page, contact us page.
Look and feel should be modern and clean and easy to navigate.
Sections for call outs for specific services: Business Marketing Strategy, Content Creation and Marketing, Graphic & Publication Design, Pay Per Click (PPC) Management, Search Engine Optimization, Social Media Management, Video Production & Editing, Website Hosting & Management, Website Design & Development
Use color from logo that was uploaded.

```html
<!DOCTYPE html>
<html lang="en">
<head>
<meta charset="utf-8">
<title>Lift Signal — Online Marketing Agency</title>
<link href="https://fonts.googleapis.com/css2?family=Poppins:wght@400;500;600;700;800&family=Roboto:wght@400;500&display=swap" rel="stylesheet">
<style>
:root{
  --red:#f5324a;
  --pink:#e0409f;
  --violet:#8b33e6;
  --navy:#0d1f3c;
  --ink:#1c1c2e;
  --text:#6d6f80;
  --muted:#9a9cab;
  --soft:#f5f5fa;
  --blue:#1f63ff;
  --orange:#ffa21f;
  --footer:#141414;
  --line:#e9e9f1;
}
*{margin:0;padding:0;box-sizing:border-box}
html,body{width:1200px;height:5069px;overflow:hidden}
body{position:relative;background:#fff;font-family:"Roboto",sans-serif;color:var(--text)}
.abs{position:absolute}
h1,h2,h3,h4{font-family:"Poppins",sans-serif;color:var(--ink)}

/* admin bar */
.admin-bar{left:0;top:0;width:1200px;height:24px;background:#1d2327;color:#eee;font-size:11px;display:flex;align-items:center;gap:22px;padding:0 14px}
.admin-bar .right{margin-left:auto}

/* header */
.brand{left:128px;top:34px;width:140px;text-align:center}
.brand-mark{width:26px;height:26px;border-radius:50%;background:var(--red);margin:0 auto 8px}
.brand-name{font-family:"Poppins",sans-serif;font-weight:600;font-size:15px;color:var(--ink);letter-spacing:.5px}
.brand-tag{font-size:8px;color:var(--muted);letter-spacing:1px}
.nav{left:400px;top:68px;display:flex;gap:22px;font-family:"Poppins",sans-serif;font-size:11px;font-weight:500;color:var(--ink)}
.nav span:first-child{color:var(--red)}
.search{left:898px;top:62px;width:26px;height:26px;border-radius:50%;border:2px solid var(--red);opacity:.7}
.phone-btn{left:940px;top:56px;width:136px;height:38px;border-radius:20px;background:#2c2fa8;color:#fff;font-size:11px;display:flex;align-items:center;justify-content:center}

/* hero */
.hero-art{left:640px;top:24px;width:560px;height:580px}
.hero-title{left:138px;top:226px;width:460px;font-size:37px;font-weight:700;line-height:1.1}
.hero-text{left:138px;top:358px;width:440px;font-size:13.5px;line-height:1.65}
.btn-red{background:var(--red);color:#fff;font-family:"Poppins",sans-serif;font-size:10px;font-weight:600;letter-spacing:1px;display:flex;align-items:center;justify-content:center}
.hero-btn{left:138px;top:470px;width:140px;height:46px}
.watch{left:300px;top:470px;display:flex;align-items:center;gap:10px;font-size:11px;color:var(--red)}
.watch i{width:44px;height:44px;border-radius:50%;background:#fde3e8;display:flex;align-items:center;justify-content:center}
.watch i b{width:22px;height:22px;border-radius:50%;background:var(--red)}

/* sem */
.sem-art{left:112px;top:650px;width:435px;height:328px}
.sem-title{left:623px;top:670px;width:460px;font-size:30px;font-weight:600;line-height:1.15;letter-spacing:.5px}
.sem-text{left:623px;top:798px;width:470px;font-size:11.5px;line-height:1.8}
.btn-outline{left:623px;top:914px;width:138px;height:40px;border:1.5px solid var(--red);border-radius:22px;color:var(--red);font-size:10px;font-weight:600;letter-spacing:1px;display:flex;align-items:center;justify-content:center;font-family:"Poppins",sans-serif}

/* services */
.services-bg{left:0;top:1060px;width:1200px;height:1120px;background:var(--soft)}
.dots{left:555px;top:1125px}
.services-title{left:0;top:1216px;width:1200px;text-align:center;font-size:30px;font-weight:600}
.services-title em{font-style:normal;color:var(--red)}
.services-sub{left:0;top:1270px;width:1200px;text-align:center;font-size:12.5px}
.card{background:#fff;box-shadow:0 2px 10px rgba(20,20,60,.07);text-align:center;padding:22px 18px}
.service-card{width:280px;height:245px}
.service-card svg{display:block;margin:0 auto 18px}
.service-card h3{font-size:13.5px;font-weight:500;margin-bottom:14px}
.service-card p{font-size:11px;line-height:1.9;color:var(--muted);height:68px}
.service-card .more{font-size:11px;color:var(--red);margin-top:18px}

/* news */
.news-bg{left:0;top:2180px;width:1200px;height:855px}
.news-label{left:0;top:2352px;width:1200px;text-align:center;color:var(--red);font-size:10px;letter-spacing:2px;font-weight:600}
.news-title{left:0;top:2380px;width:1200px;text-align:center;color:#fff;font-size:32px;font-weight:500}
.news-line{left:599px;top:2434px;width:2px;height:46px;background:var(--red)}
.news-card{width:296px;background:#fff;padding:50px 32px 0 32px}
.news-meta{font-size:10px;color:var(--muted);display:flex;gap:24px;margin-bottom:18px}
.news-card h3{font-size:13.5px;font-weight:600;margin-bottom:38px}
.news-card p{font-size:11px;line-height:1.9;color:var(--text)}
.btn-blue{display:inline-flex;width:118px;height:34px;background:var(--blue);color:#fff;font-size:10.5px;align-items:center;justify-content:center;margin-top:24px;border-radius:2px}

/* about */
.about-art{left:213px;top:3210px;width:912px;height:455px}
.about-card{left:133px;top:3150px;width:448px;height:460px;background:#fff;box-shadow:0 4px 24px rgba(20,20,60,.1);padding:46px 40px}
.about-label{color:var(--red);font-size:10px;letter-spacing:1.5px;font-weight:600}
.about-card h2{font-size:28px;font-weight:500;margin:12px 0 14px}
.about-card p{font-size:11px;line-height:2;margin-bottom:24px}
.bar{margin-bottom:30px}
.bar-head{display:flex;justify-content:space-between;font-size:10.5px;color:var(--ink);margin-bottom:8px}
.bar-track{height:6px;background:#eee;border-radius:3px}
.bar-fill{height:6px;border-radius:3px}

/* testimonials */
.testi-wave{left:840px;top:3720px;width:360px;height:320px}
.testi-label{left:0;top:3806px;width:1200px;text-align:center;color:var(--red);font-size:11px;letter-spacing:1.5px;font-weight:600}
.testi-title{left:0;top:3848px;width:1200px;text-align:center;font-size:38px;font-weight:500}
.testi-card{width:296px;height:295px;background:#fff;box-shadow:0 4px 18px rgba(20,20,60,.08);padding:60px 26px 0;text-align:left}
.stars{color:var(--orange);font-size:13px;letter-spacing:2px}
.quote{position:absolute;right:26px;top:38px;font-family:"Poppins",sans-serif;font-size:56px;color:#e2e0f3;line-height:1}
.person{display:flex;align-items:center;gap:14px;margin:18px 0 24px}
.avatar{width:48px;height:48px;border-radius:50%}
.person h4{font-size:13.5px;font-weight:600}
.person small{font-size:10px;color:var(--muted)}
.testi-card p{font-size:11px;line-height:1.9}
.pager{left:570px;top:4340px;display:flex;gap:8px}
.pager i{width:6px;height:6px;border-radius:50%;background:#d9d9e6}
.pager i:first-child{background:var(--red)}

/* stats */
.stats-label{left:138px;top:4470px;font-size:9.5px;font-weight:600;color:var(--ink);letter-spacing:1px;display:flex;align-items:center;gap:10px}
.stats-label b{width:30px;height:2px;background:var(--orange)}
.stats-title{left:138px;top:4500px;font-size:42px;font-weight:800;line-height:1.15}
.stat{top:4520px}
.stat strong{font-family:"Poppins",sans-serif;font-size:38px;font-weight:500;color:var(--ink)}
.stat sup{color:var(--orange);font-size:14px}
.stat div{font-size:10px;color:var(--orange)}

/* footer */
.footer{left:0;top:4645px;width:1200px;height:424px;background:var(--footer);color:#ddd}
.fcol{top:95px;font-size:11px;line-height:1.6}
.fcol h4{color:#fff;font-size:13px;font-weight:500;margin-bottom:18px}
.fcol p{margin-bottom:10px}
.social{display:flex;gap:12px}
.social i{width:26px;height:26px;border-radius:50%}
.flogo{left:133px;top:290px;display:flex;align-items:center;gap:8px;color:#fff;font-family:"Poppins",sans-serif;font-size:10px;font-weight:600}
.flogo i{width:16px;height:16px;border-radius:50%;background:var(--red)}
.fcopy{right:130px;top:292px;font-size:10px}
.fbottom{left:0;top:395px;width:1200px;height:29px;background:#0b0b0b;font-size:9px;color:#aaa;display:flex;align-items:center;justify-content:center}

/* scroll-to-top boxes */
.top-btn{left:1150px;width:32px;height:32px;background:#c8c8cf;display:flex;align-items:center;justify-content:center}
.top-btn.dark{background:#0a1830}
.top-btn::before{content:"";border-left:5px solid transparent;border-right:5px solid transparent;border-bottom:6px solid #fff}
</style>
</head>
<body>

<div class="abs admin-bar"><span>My Blog</span><span>Customize</span><span>0</span><span>+ New</span><span>Edit Page</span><span>Edit with Builder</span><span class="right">Howdy, rowan</span></div>

<!-- header -->
<div class="abs brand"><div class="brand-mark"></div><div class="brand-name">LIFT SIGNAL</div><div class="brand-tag">Internet Marketing Experts</div></div>
<nav class="abs nav"><span>HOME</span><span>ABOUT US</span><span>BLOG</span><span>SERVICES</span><span>CONTACT US</span></nav>
<div class="abs search"></div>
<div class="abs phone-btn">+1 555 010 233</div>

<!-- hero -->
<svg class="abs hero-art" viewBox="0 0 560 580" role="img" aria-label="Illustration of a marketing team working at laptops in front of a large analytics dashboard">
  <defs><linearGradient id="heroGrad" x1="0" y1="0" x2="1" y2="1"><stop offset="0" stop-color="#8b33e6"/><stop offset=".55" stop-color="#e0409f"/><stop offset="1" stop-color="#f26aa8"/></linearGradient></defs>
  <path d="M210 0 H560 V560 C470 600 360 560 320 470 C280 380 120 360 60 260 C10 170 110 90 210 0 Z" fill="url(#heroGrad)"/>
</svg>
<h1 class="abs hero-title">Lift Signal Is A Full-Service Online Marketing Agency.</h1>
<p class="abs hero-text">We can handle any element of your online marketing so you can get back to doing what you do best — growing your business. All of our services are offered on an 'a la carte' basis.</p>
<div class="abs btn-red hero-btn">READ MORE</div>
<div class="abs watch"><i><b></b></i>Watch Video</div>

<!-- sem -->
<svg class="abs sem-art" viewBox="0 0 435 328" role="img" aria-label="Illustration of a strategist reviewing charts on wall screens">
  <circle cx="250" cy="190" r="170" fill="#f1f1f4"/>
  <rect x="0" y="30" width="150" height="160" fill="#2a2a3a"/>
  <rect x="170" y="30" width="210" height="80" fill="#2a2a3a"/>
  <rect x="150" y="60" width="90" height="240" fill="#3c3a78" opacity=".85"/>
</svg>
<h2 class="abs sem-title">We Are An SEM Company That Specializes In Developing.</h2>
<p class="abs sem-text">Lorem ipsum dolor sit amet, consectetur adipiscing elit, sed do eiusmod tempor incididunt ut labore et dolore magna aliqua. Ut consequat semper viverra nam libero. Ipsum nunc aliquet bibendum enim facilisis gravida neque convallis. Mattis rhoncus urna neque viverra justo.</p>
<div class="abs btn-outline">LEARN MORE</div>

<!-- services -->
<div class="abs services-bg"></div>
<svg class="abs dots" width="90" height="75" viewBox="0 0 90 75" aria-hidden="true">
  <g fill="#8a86d6"><circle cx="8" cy="68" r="2"/><circle cx="20" cy="62" r="2"/><circle cx="32" cy="56" r="2"/><circle cx="44" cy="48" r="2"/><circle cx="56" cy="40" r="2"/><circle cx="68" cy="30" r="2"/><circle cx="80" cy="18" r="2"/><circle cx="44" cy="62" r="2"/><circle cx="56" cy="56" r="2"/><circle cx="68" cy="50" r="2"/><circle cx="80" cy="42" r="2"/></g>
</svg>
<h2 class="abs services-title">WHAT WE DO AT <em>Lift Signal</em></h2>
<p class="abs services-sub">See how we're helping business grow.</p>

<div class="abs card service-card" style="left:150px;top:1335px"><svg width="30" height="30"><rect x="5" y="7" width="18" height="18" fill="none" stroke="#3d63d8" stroke-width="2"/><path d="M12 18 L25 5" stroke="#3d63d8" stroke-width="2"/></svg><h3>Content Creation and Marketing</h3><p>You've heard it before. "Content is king." Search engines love it and customers expect it...</p><div class="more">Learn More</div></div>
<div class="abs card service-card" style="left:461px;top:1335px"><svg width="30" height="30"><circle cx="13" cy="13" r="8" fill="none" stroke="#ff8a00" stroke-width="2.5"/><path d="M19 19 L26 26" stroke="#ff8a00" stroke-width="3"/></svg><h3>Business Marketing Strategy</h3><p>Let us strategize the big picture for you. With decades of experience...</p><div class="more">Learn More</div></div>
<div class="abs card service-card" style="left:772px;top:1335px"><svg width="30" height="30"><path d="M4 7 L15 10 L26 7 V24 L15 27 L4 24 Z" fill="#e0132b"/></svg><h3>Graphic &amp; Publication Design</h3><p>Our designers have decades of experience in everything...</p><div class="more">Learn More</div></div>

<div class="abs card service-card" style="left:150px;top:1595px"><svg width="30" height="30"><circle cx="15" cy="15" r="11" fill="none" stroke="#36c46f" stroke-width="2"/><circle cx="15" cy="15" r="5" fill="none" stroke="#36c46f" stroke-width="2"/></svg><h3>Pay Per Click (PPC) Management</h3><p>PPC advertising delivers some of the best ROI online...</p><div class="more">Learn More</div></div>
<div class="abs card service-card" style="left:461px;top:1595px"><svg width="30" height="30"><rect x="4" y="6" width="20" height="16" fill="none" stroke="#4a8de8" stroke-width="2"/><circle cx="20" cy="21" r="5" fill="none" stroke="#4a8de8" stroke-width="2"/></svg><h3>Search Engine Optimization</h3><p>The SEO playing field is shifting constantly. From week to week...</p><div class="more">Learn More</div></div>
<div class="abs card service-card" style="left:772px;top:1595px"><svg width="30" height="30"><circle cx="15" cy="15" r="11" fill="#1f7ae8"/><path d="M9 17 L13 12 L17 16 L21 12" stroke="#fff" stroke-width="2" fill="none"/></svg><h3>Social Media Management</h3><p>Scratching your head over how to make social media work for...</p><div class="more">Learn More</div></div>

<div class="abs card service-card" style="left:150px;top:1855px"><svg width="30" height="30"><rect x="4" y="7" width="22" height="16" rx="2" fill="none" stroke="#ff8a3d" stroke-width="2"/><path d="M13 11 L19 15 L13 19 Z" fill="#ff8a3d"/></svg><h3>Video Production &amp; Editing</h3><p>Video content is absolutely key in today's SEO landscape...</p><div class="more">Learn More</div></div>
<div class="abs card service-card" style="left:461px;top:1855px"><svg width="30" height="30"><circle cx="11" cy="19" r="6" fill="none" stroke="#b04ee0" stroke-width="2"/><circle cx="20" cy="10" r="6" fill="none" stroke="#b04ee0" stroke-width="2"/></svg><h3>Website Hosting &amp; Management</h3><p>We will find you the most affordable, most-appropriate-for-your-business...</p><div class="more">Learn More</div></div>
<div class="abs card service-card" style="left:772px;top:1855px"><svg width="30" height="30"><circle cx="15" cy="15" r="12" fill="#e6ebf8"/><rect x="9" y="9" width="12" height="12" fill="none" stroke="#6c83c9" stroke-width="2"/></svg><h3>Website Design &amp; Development</h3><p>Nothing will kill your business faster than a dated, unattractive or confusing website...</p><div class="more">Learn More</div></div>

<!-- news -->
<svg class="abs news-bg" viewBox="0 0 1200 855" preserveAspectRatio="none" aria-hidden="true"><path d="M0 40 L1200 0 V855 H0 Z" fill="var(--navy)"/></svg>
<div class="abs news-label">LATEST NEWS</div>
<h2 class="abs news-title">Our Latest News</h2>
<div class="abs news-line"></div>

<div class="abs news-card" style="left:133px;top:2533px;height:402px"><div class="news-meta"><span>rowan</span><span>July 24, 2020</span></div><h3>Content Creation and Marketing</h3><p>Content is King. It's almost a cliché after all these years, but it still holds true. Search engines love good content and in fact, websites with poor quality content can expect to be penalized. In this digital, mobile "always on" age of marketing...</p><span class="btn-blue">Learn more</span></div>
<div class="abs news-card" style="left:452px;top:2533px;height:422px"><div class="news-meta"><span>rowan</span><span>July 24, 2020</span></div><h3>Pay Per Click (PPC) Management</h3><p>Pay Per Click advertising is straightforward and powerful. It delivers some of the best ROI of any digital marketing method. Plus, there is a good chance your competitors aren't properly using PPC, which gives you an edge if you know what...</p><span class="btn-blue">Learn more</span></div>
<div class="abs news-card" style="left:771px;top:2533px;height:402px"><div class="news-meta"><span>rowan</span><span>July 24, 2020</span></div><h3>Social Media Management</h3><p>Over 2 billion people around the world are active on social media, which includes 70% of the population of the US. More than 50% of adults have two or more social media profiles. Businesses spend nearly $10 billion on social...</p><span class="btn-blue">Learn more</span></div>

<!-- about -->
<svg class="abs about-art" viewBox="0 0 912 455" preserveAspectRatio="none" role="img" aria-label="Isometric illustration of glowing data platforms and rising bar charts">
  <defs><linearGradient id="aboutGrad" x1="0" y1="0" x2="1" y2="1"><stop offset="0" stop-color="#2a1470"/><stop offset=".6" stop-color="#3a1a8a"/><stop offset="1" stop-color="#2a1470"/></linearGradient></defs>
  <rect width="912" height="455" fill="url(#aboutGrad)"/>
  <ellipse cx="560" cy="210" rx="160" ry="140" fill="#e0336b" opacity=".35"/>
</svg>
<div class="abs about-card">
  <div class="about-label">ABOUT US</div>
  <h2>World's best solution</h2>
  <p>At the coast of the Semantics, a large language ocean. A small river named Consonantia, there live the blind texts. Separated they live in Bookmarksgrove far away, behind the word mountains far from the countries.</p>
  <div class="bar"><div class="bar-head"><span>Video Editing</span><span>90%</span></div><div class="bar-track"><div class="bar-fill" style="width:90%;background:#22c56b"></div></div></div>
  <div class="bar"><div class="bar-head"><span>Web Hosting</span><span>95%</span></div><div class="bar-track"><div class="bar-fill" style="width:95%;background:#ffa21f"></div></div></div>
  <div class="bar"><div class="bar-head"><span>Social Media Management</span><span>98%</span></div><div class="bar-track"><div class="bar-fill" style="width:98%;background:#20c9e0"></div></div></div>
</div>

<!-- testimonials -->
<svg class="abs testi-wave" viewBox="0 0 360 320" aria-hidden="true"><path d="M80 40 C180 0 300 20 360 60 V320 C260 300 120 260 80 160 C60 110 40 60 80 40 Z" fill="#eef4ff"/><path d="M112 108 L126 96 L124 114 Z" fill="none" stroke="#e88aa6" stroke-width="2"/></svg>
<div class="abs testi-label">Testimonial</div>
<h2 class="abs testi-title">What's Our Client Say</h2>

<div class="abs testi-card" style="left:135px;top:3975px"><span class="quote">”</span><div class="stars">★★★★★</div><div class="person"><div class="avatar" style="background:#5a9bd6" role="img" aria-label="Client portrait"></div><div><h4>Mara Quinn</h4><small>Web Developer</small></div></div><p>Behind the word mountains from the countries Vokalia and Consonantia, there live the blind texts. Separated they live.</p></div>
<div class="abs testi-card" style="left:452px;top:3975px"><span class="quote">”</span><div class="stars">★★★★★</div><div class="person"><div class="avatar" style="background:#2d2d3a" role="img" aria-label="Client portrait"></div><div><h4>Theo Lang</h4><small>Web Developer</small></div></div><p>Behind the word mountains from the countries Vokalia and Consonantia, there live the blind texts. Separated they live.</p></div>
<div class="abs testi-card" style="left:768px;top:3975px"><span class="quote">”</span><div class="stars">★★★★★</div><div class="person"><div class="avatar" style="background:#f3c95a" role="img" aria-label="Client portrait"></div><div><h4>Nadia Brooks</h4><small>Web Developer</small></div></div><p>Behind the word mountains from the countries Vokalia and Consonantia, there live the blind texts. Separated they live.</p></div>
<svg class="abs" style="left:436px;top:4238px" width="40" height="40" aria-hidden="true"><circle cx="20" cy="20" r="15" fill="none" stroke="#e6336f" stroke-width="4"/></svg>
<div class="abs pager"><i></i><i></i><i></i><i></i></div>

<!-- stats -->
<div class="abs stats-label"><b></b>EXPLORE OUR EXPERT</div>
<h2 class="abs stats-title">Our Business<br>Statistics</h2>
<div class="abs stat" style="left:522px"><strong>16,548</strong><sup>+</sup><div>Support Given</div></div>
<div class="abs stat" style="left:765px"><strong>254</strong><sup>+</sup><div>Clients Rating</div></div>
<div class="abs stat" style="left:960px"><strong>2M</strong><sup>+</sup><div>Money Saved</div></div>

<!-- footer -->
<footer class="abs footer">
  <div class="abs fcol" style="left:133px"><h4>Shop</h4><p>12 Maple Row<br>NORTHFIELD<br>AB1 2CD</p></div>
  <div class="abs fcol" style="left:370px"><h4>Contact</h4><p>✉ &nbsp;hello@liftsignal.com</p><p>☏ &nbsp;0100 55501 0199</p></div>
  <div class="abs fcol" style="left:608px"><h4>Quick Links</h4><p>About Us</p><p>Contact Us</p><p>Privacy Policy</p></div>
  <div class="abs fcol" style="left:845px"><h4>Social</h4><div class="social"><i style="background:#3b5bb5"></i><i style="background:#2a9de8"></i><i style="background:#e0223a"></i></div></div>
  <div class="abs flogo"><i></i>LIFT SIGNAL</div>
  <div class="abs fcopy">© Copyright 2019 Brightkit. All right reserved.</div>
  <div class="abs fbottom">Copyright Harbor Theme by Nolan</div>
</footer>

<!-- scroll-to-top -->
<div class="abs top-btn" style="top:566px"></div>
<div class="abs top-btn" style="top:968px"></div>
<div class="abs top-btn" style="top:1418px"></div>
<div class="abs top-btn" style="top:1868px"></div>
<div class="abs top-btn dark" style="top:2318px"></div>
<div class="abs top-btn dark" style="top:2768px"></div>
<div class="abs top-btn" style="top:3218px"></div>
<div class="abs top-btn" style="top:3668px"></div>
<div class="abs top-btn" style="top:4118px"></div>
<div class="abs top-btn" style="top:4568px"></div>
</body>
</html>
```